Kestrel Signs Facebook Banner Design

Design a facebook banner for a sign company. I would like to have a modern approach to it.

Product Offering:
Signs
Banners
Decals
Commercial Wraps

```html
<!DOCTYPE html>
<html lang="en">
<head>
<meta charset="UTF-8">
<title>Kestrel Signs – Facebook Banner</title>
<link rel="stylesheet" href="https://fonts.googleapis.com/css2?family=Exo+2:ital,wght@0,800;0,900;1,800;1,900&display=swap">
<style>
  :root {
    --paper: #f2f2f2;
    --ink: #4a4a4c;
    --red: #e8383d;
    --coral: #f0654a;
    --orange: #fc8d4a;
    --lemon: #fdfa9d;
    --url-yellow: #fdf57a;
    --white: #ffffff;
  }
  html, body {
    margin: 0;
    padding: 0;
    overflow: hidden;
    background: var(--paper);
  }
  .banner {
    position: relative;
    width: 1200px;
    height: 457px;
    background: var(--paper);
    overflow: hidden;
    font-family: "Exo 2", "Arial Black", sans-serif;
  }

  /* Brand block */
  .brand {
    position: absolute;
    left: 90px;
    top: 28px;
    width: 380px;
    text-align: center;
  }
  .brand-name {
    margin: 0;
    color: var(--red);
    font-weight: 900;
    font-size: 46px;
    line-height: 46px;
    letter-spacing: 1px;
    text-transform: uppercase;
  }
  .brand-name span { display: block; }
  .brand-name .second { font-size: 40px; line-height: 42px; }

  /* Headline */
  .headline {
    position: absolute;
    left: 60px;
    top: 172px;
    width: 440px;
    margin: 0;
    text-align: center;
    font-style: italic;
    font-weight: 900;
    text-transform: uppercase;
    line-height: 1;
  }
  .headline span { display: block; }
  .headline .lead { color: var(--ink); font-size: 32px; letter-spacing: 1px; }
  .headline .accent { color: var(--red); font-size: 44px; margin-top: 4px; }
  .headline .main { color: var(--ink); font-size: 66px; margin-top: 2px; letter-spacing: 1px; }

  /* Web address bar */
  .web-bar {
    position: absolute;
    left: 76px;
    top: 366px;
    width: 414px;
    height: 32px;
  }
  .web-bar svg { position: absolute; inset: 0; }
  .web-bar .url {
    position: relative;
    display: block;
    text-align: center;
    line-height: 32px;
    color: var(--url-yellow);
    font-style: italic;
    font-weight: 900;
    font-size: 21px;
    letter-spacing: 0.5px;
  }

  /* Product offering */
  .offering-label {
    position: absolute;
    left: 546px;
    top: 19px;
    width: 57px;
    height: 417px;
    background: var(--ink);
    display: flex;
    align-items: center;
    justify-content: center;
  }
  .offering-label span {
    writing-mode: vertical-rl;
    transform: rotate(180deg);
    color: var(--white);
    font-style: italic;
    font-weight: 900;
    font-size: 23px;
    letter-spacing: 1px;
    text-transform: uppercase;
    white-space: nowrap;
  }
  .products {
    position: absolute;
    left: 603px;
    top: 0;
    width: 597px;
    height: 457px;
    display: flex;
    margin: 0;
    padding: 0;
    list-style: none;
  }
  .product {
    flex: 1;
    display: flex;
    align-items: center;
    justify-content: center;
  }
  .product span {
    writing-mode: vertical-rl;
    transform: rotate(180deg);
    color: var(--white);
    font-style: italic;
    font-weight: 900;
    font-size: 56px;
    line-height: 0.9;
    letter-spacing: 1px;
    text-transform: uppercase;
    text-align: center;
    white-space: nowrap;
  }
  .product--signs { background: var(--red); }
  .product--banners { background: var(--coral); }
  .product--decals { background: var(--orange); }
  .product--wraps { background: var(--lemon); }
  .product--wraps span { color: var(--red); font-size: 46px; }
</style>
</head>
<body>
  <div class="banner">
    <div class="brand">
      <h1 class="brand-name"><span>Kestrel</span><span class="second">Signs</span></h1>
    </div>

    <h2 class="headline">
      <span class="lead">We are</span>
      <span class="accent">Signage</span>
      <span class="main">Company</span>
    </h2>

    <div class="web-bar">
      <svg width="414" height="32" viewBox="0 0 414 32" aria-hidden="true">
        <polygon points="14,0 414,0 400,32 0,32" fill="#4a4a4c"/>
      </svg>
      <span class="url">WWW.WEBSITENAME.COM</span>
    </div>

    <div class="offering-label"><span>Product Offering</span></div>

    <ul class="products">
      <li class="product product--signs"><span>Signs</span></li>
      <li class="product product--banners"><span>Banners</span></li>
      <li class="product product--decals"><span>Decals</span></li>
      <li class="product product--wraps"><span>Commercial<br>Wraps</span></li>
    </ul>
  </div>
</body>
</html>
```